Tarrow Building Performance

Id like for my business card to be very bold and professional. Incorporating the business logo, the main services offered, and my contact info. Services are spray foam, insulation, new construction, retrofit, weatherization.

When opening this project sketch harbor was not able to upload my new logo that I picked from another recent sketch harbor project. Does anyone know how i could upload my logo onto the page for design of the business cards?

Target Market(s)

Building owners, contractors

Industry/Entity Type

Building Insulation and performance improvements

Contact Information for Business Card

Owner, Email dean@tarrowbuildingperformance.example Phone number 555-208-6147

Colors
0054AA
0677BA
7BADD7
CADEEF
E8F1F8
F0912C
F2A743
F7CA91
FBE8D2
FDF5EE

Requirements
Must have
• Services- spray foam, cellulose, mineral wool, fiberglass, air sealing, new construction, retrofit, weatherization, energy saving assesments

```html
<!DOCTYPE html>
<html lang="en">
<head>
<meta charset="utf-8">
<title>Tarrow Building Performance – Business Card</title>
<link rel="stylesheet" href="https://fonts.googleapis.com/css2?family=Montserrat:wght@400;500;600;800&display=swap">
<style>
  :root {
    --page-bg: #e9e6e1;
    --navy: #0b1533;
    --navy-deep: #081029;
    --orange: #f0912c;
    --orange-dark: #c96f12;
    --orange-light: #f2a743;
    --sky: #2ea9e6;
    --white: #ffffff;
    --text-light: #e8f1f8;
  }
  * { box-sizing: border-box; margin: 0; padding: 0; }
  html, body {
    width: 1200px; height: 900px; overflow: hidden;
    background: var(--page-bg);
    font-family: "Montserrat", sans-serif;
  }
  .canvas {
    width: 1200px; height: 900px;
    display: flex; flex-direction: column; align-items: center; justify-content: center;
    gap: 40px;
  }
  .card {
    position: relative;
    width: 660px; height: 377px;
    border-radius: 34px;
    overflow: hidden;
    box-shadow: 0 10px 26px rgba(0,0,0,0.22);
  }

  /* Back side */
  .card-back { background: var(--orange); }
  .pattern-fill {
    position: absolute; inset: 0;
    background: radial-gradient(ellipse at 60% 45%, var(--orange-light) 0%, var(--orange) 45%, var(--orange-dark) 100%);
  }
  .back-name {
    position: absolute; right: 96px; top: 168px;
    color: var(--white);
    font-weight: 800; font-size: 20px; letter-spacing: 0.5px;
  }

  /* Front side */
  .card-front {
    background: linear-gradient(160deg, var(--navy-deep) 0%, var(--navy) 60%, #141a35 100%);
    color: var(--text-light);
  }
  .contact {
    position: absolute; left: 36px; top: 128px;
    white-space: nowrap;
  }
  .contact-name {
    font-size: 19px; font-weight: 500; color: var(--orange); letter-spacing: 0.5px;
  }
  .contact-name .divider { color: var(--orange); margin: 0 6px; }
  .contact-role { color: var(--white); font-size: 15px; font-weight: 400; letter-spacing: 0; }
  .contact-line {
    display: flex; align-items: center; gap: 9px;
    margin-top: 8px; font-size: 13px; color: var(--white);
  }
  .contact-line svg { width: 15px; height: 15px; flex: none; }

  .services {
    position: absolute; right: 34px; top: 40px; width: 250px;
    white-space: nowrap;
  }
  .services-title {
    color: var(--sky); font-weight: 600; font-size: 17px; letter-spacing: 0.5px;
    margin-bottom: 6px;
  }
  .services-list { list-style: none; }
  .services-list li {
    font-size: 14px; color: var(--white); line-height: 1.6;
  }
  .services-list .dot { color: var(--orange); margin: 0 5px; font-size: 10px; vertical-align: 2px; }
  .services-rule {
    height: 2px; background: var(--sky); margin-top: 8px; width: 240px;
  }

  .brand {
    position: absolute; right: 44px; bottom: 46px;
    display: flex; align-items: center; gap: 16px;
  }
  .brand-mark {
    width: 44px; height: 44px; background: var(--sky);
  }
  .brand-name {
    color: var(--orange); font-weight: 800; font-size: 28px; line-height: 1.05;
    text-transform: uppercase; letter-spacing: 0.5px;
    white-space: nowrap;
  }
  .brand-rule {
    position: absolute; right: 44px; bottom: 30px; width: 330px; height: 5px; background: var(--sky);
  }
</style>
</head>
<body>
<main class="canvas">

  <section class="card card-back" aria-label="Business card back">
    <div class="pattern-fill" role="img" aria-label="Repeating embossed pattern of the company mark on orange"></div>
    <span class="back-name">Tarrow</span>
  </section>

  <section class="card card-front" aria-label="Business card front">
    <div class="contact">
      <p class="contact-name">DEAN<span class="divider">|</span><span class="contact-role">Owner</span></p>
      <p class="contact-line">
        <svg viewBox="0 0 24 24" aria-hidden="true"><path fill="#2ea9e6" d="M6.6 10.8a15.1 15.1 0 0 0 6.6 6.6l2.2-2.2c.3-.3.7-.4 1-.2 1.1.4 2.300.6 3.600.6.6 0 1 .4 1 1V20c0 .6-.4 1-1 1A17 17 0 0 1 3 4c0-.6.4-1 1-1h3.5c.6 0 1 .4 1 1 0 1.3.2 2.5.6 3.6.1.3 0 .7-.2 1z"/></svg>
        555-208-6147
      </p>
      <p class="contact-line">
        <svg viewBox="0 0 24 24" aria-hidden="true"><path fill="#2ea9e6" d="M3 5h18v14H3zm2 2v.5l7 4.5 7-4.5V7zm0 2.8V17h14V9.8l-7 4.5z"/></svg>
        dean@tarrowbuildingperformance.example
      </p>
    </div>

    <div class="services">
      <h2 class="services-title">SERVICES</h2>
      <ul class="services-list">
        <li><span class="dot">◆</span>Spray Foam<span class="dot">◆</span>Cellulose</li>
        <li><span class="dot">◆</span>Mineral Wool<span class="dot">◆</span>Fiberglass</li>
        <li><span class="dot">◆</span>Air Sealing<span class="dot">◆</span>New Construction</li>
        <li><span class="dot">◆</span>Retrofit<span class="dot">◆</span>Weatherization</li>
        <li><span class="dot">◆</span>Energy Saving Assesments</li>
      </ul>
      <div class="services-rule"></div>
    </div>

    <div class="brand">
      <span class="brand-mark" aria-hidden="true"></span>
      <p class="brand-name">Tarrow<br>Building Performance</p>
    </div>
    <div class="brand-rule" aria-hidden="true"></div>
  </section>

</main>
</body>
</html>
```